Sports Graphic Templates for Action Photos

I am looking for a graphic design template for sports action photos. This needs to be simple enough that someone without expertise in Photoshop (use this program) can upload an image into a layer or what not and export the file for use.

The file needs to be 1280x720 and MUST incorporate the attached QUILLS graphic in some form or fashion. How is up to you.

Orbitron and DinPro are the two fonts I want to have used in the design. It can be one or it can be both.

Ideally - this template can be used for multiple graphics using similar action shots. Athlete of the Week or Athlete of the Year are two examples.

One other note - the QUILLS graphic needs to be incorporated somehow and it would be good to be able to interchange the coloring. The file uploaded is blue but we'd like to be able to match the colors to other photos or pull coloring from other parts of the image.

The image or action shot must not be cut out or altered other than to have certain styles applied. As mentioned above this would need to be updated by someone with limited Photoshop knowledge.

Examples:

http://www.hoopvarta.com/falconers/releases/player-of-the-week-doran-160404

https://tessmorathletics.com/news/2017/10/9/womens-soccer-lisa-varnet-adds-another-coral-ridge-player-of-the-week-award.aspx?path=wsoc

http://www.hoopvarta.com/tavin-week

https://k7pwm2zrfaqo58.imgvaultcdn.net/900x407_/media/14124/2560x1300-potywinner-belcastro.jpg

https://morvenhawks.com/images/2017/5/15/SB_Lakeshore_9_Awards_Social_Media_Graphic_Greta_Solvik_v1.jpg

https://thumbs-qx4.pictorelay.net/images?q=tbn:Vx82hTqLm04-77pR3KWdsZeBn91CfuAh56JoNwYtLqEaQ3XKrb9m

Target Market(s)

Action Shots Highlighting Achievement

Font styles to use
Other font styles liked:
• Orbitron and DinPro - one or both of those

Colors

Designer to choose colors to be used in the design.

Requirements
Must have
• Photoshop design. Use of the QUILLS graphis supplied - fonts (one or both) - 1280x720 sizing.
• Easy to use - someone with limited knowledge can easily update.
Nice to have
• Something that stands out from the rest. Examples were shown - none of those incorporate an action shot without the cutting out of the action or person in the image.
Should not have
• Any non-free textures or other items that need to be purchased.

```html
<!DOCTYPE html>
<html lang="en">
<head>
<meta charset="utf-8">
<title>Athlete of the Week – Template Overview</title>
<link href="https://fonts.googleapis.com/css2?family=Barlow:wght@400;600;700;800&display=swap" rel="stylesheet">
<style>
  :root {
    --quill-deep: #3a0fd6;
    --quill-mid: #5a2cf2;
    --quill-light: #8a68ff;
    --quill-stripe: rgba(255,255,255,0.10);
    --slate: #1c252a;
    --white: #ffffff;
    --silver-hi: #ffffff;
    --silver-lo: #8d8d98;
    --accent-red: #e8806e;
    --panel-bg: #f0f0f0;
    --panel-line: #dcdcdc;
    --panel-text: #333333;
    --row-flag: #f08474;
  }
  * { margin: 0; padding: 0; box-sizing: border-box; }
  html, body { width: 1200px; height: 1200px; overflow: hidden; background: var(--slate); }
  body { font-family: "Barlow", Arial, sans-serif; position: relative; }

  .banner {
    position: absolute; left: 0; top: 0; width: 1200px; height: 675px; overflow: hidden;
    background: radial-gradient(ellipse at 70% 40%, var(--quill-mid) 0%, var(--quill-deep) 70%);
  }
  .banner .quills { position: absolute; inset: 0; }
  .action-shot {
    position: absolute; left: 330px; top: 40px; width: 600px; height: 560px;
    background: radial-gradient(ellipse at 62% 45%, rgba(40,110,170,0.75) 0%, rgba(70,60,150,0.55) 40%, rgba(90,50,230,0) 72%);
  }
  .title {
    position: absolute; left: 108px; top: 366px; line-height: 1;
    background: linear-gradient(180deg, var(--silver-hi) 10%, #d8d8e0 48%, var(--silver-lo) 60%, #e6e6ee 90%);
    -webkit-background-clip: text; background-clip: text; color: transparent;
    filter: drop-shadow(2px 3px 0 rgba(40,20,90,0.55));
  }
  .title-main { display: block; font-weight: 800; font-size: 118px; letter-spacing: -2px; }
  .title-sub { display: block; font-weight: 400; font-size: 72px; letter-spacing: 5px; margin-top: -6px; }
  .name-band {
    position: absolute; left: 95px; top: 550px; width: 470px; height: 61px;
    background: linear-gradient(90deg, rgba(255,255,255,0) 0%, rgba(255,255,255,0.12) 25%, rgba(255,255,255,0.12) 70%, rgba(255,255,255,0) 100%);
    display: flex; align-items: center; justify-content: center;
  }
  .athlete-name { color: var(--white); font-weight: 700; font-size: 31px; letter-spacing: 1px; }

  .overview-heading {
    position: absolute; left: 0; width: 890px; top: 884px; text-align: center;
    color: var(--white); font-weight: 700; font-size: 47px; letter-spacing: 1px;
  }
  .overview-key {
    position: absolute; left: 0; width: 890px; top: 948px; text-align: center;
    color: var(--white); font-weight: 700; font-size: 30px; letter-spacing: 0.5px;
  }
  .overview-key .flag { color: var(--accent-red); }

  .layers {
    position: absolute; left: 860px; top: 820px; width: 207px;
    background: var(--panel-bg); box-shadow: 0 4px 14px rgba(0,0,0,0.4);
    list-style: none;
  }
  .layer {
    height: 25.5px; display: flex; align-items: center; border-bottom: 1px solid var(--panel-line);
    font-size: 9.5px; color: var(--panel-text); position: relative;
  }
  .layer .vis { width: 29px; height: 100%; display: flex; align-items: center; justify-content: center; border-right: 1px solid var(--panel-line); }
  .layer.is-editable .vis { background: var(--row-flag); }
  .layer .thumb { width: 30px; height: 17px; margin: 0 8px 0 4px; border: 1px solid #999; background: repeating-conic-gradient(#ddd 0 25%, #fff 0 50%) 0 0 / 6px 6px; }
  .layer .thumb.photo { background: #6a4a3a; }
  .layer .thumb.white { background: #fff; }
  .layer .thumb.swatch { width: 15px; height: 15px; margin: 0 14px 0 11px; border: none; background: var(--quill-deep); }
  .layer .glyph-t { width: 30px; margin: 0 8px 0 4px; text-align: center; font-family: Georgia, serif; font-weight: 700; font-size: 11px; }
  .layer .folder { margin: 0 10px 0 2px; }
  .layer .lock { position: absolute; right: 14px; }
  .layer .italic { font-style: italic; }
</style>
</head>
<body>

<section class="banner">
  <svg class="quills" width="1200" height="675" viewBox="0 0 1200 675" aria-hidden="true">
    <g stroke="var(--quill-stripe)" fill="none">
      <line x1="-200" y1="-20" x2="520" y2="700" stroke-width="60"/>
      <line x1="-120" y1="-200" x2="760" y2="680" stroke-width="26"/>
      <line x1="-300" y1="150" x2="300" y2="750" stroke-width="40"/>
      <line x1="100" y1="-80" x2="900" y2="720" stroke-width="14"/>
      <line x1="-350" y1="300" x2="100" y2="750" stroke-width="22"/>
      <line x1="700" y1="140" x2="1300" y2="740" stroke-width="30"/>
      <line x1="900" y1="80" x2="1500" y2="680" stroke-width="12"/>
    </g>
    <g stroke="rgba(40,0,140,0.35)" fill="none">
      <line x1="-60" y1="40" x2="600" y2="700" stroke-width="4"/>
      <line x1="40" y1="-120" x2="840" y2="680" stroke-width="3"/>
      <line x1="-250" y1="270" x2="160" y2="680" stroke-width="3"/>
    </g>
  </svg>
  <div class="action-shot" role="img" aria-label="Action photo of a wheelchair racer in a helmet leaning forward, with a faded second shot of the athlete behind"></div>
  <h1 class="title">
    <span class="title-main">ATHLETE</span>
    <span class="title-sub">OF THE WEEK</span>
  </h1>
  <div class="name-band"><span class="athlete-name">TEO MARLOW</span></div>
</section>

<h2 class="overview-heading">CURRENT LAYER STRUCTURE</h2>
<p class="overview-key"><span class="flag">LIGHT RED</span> = ONES TO BE EDITED</p>

<svg width="0" height="0" style="position:absolute" aria-hidden="true">
  <symbol id="eye" viewBox="0 0 12 8"><path d="M0 4 Q6 -2 12 4 Q6 10 0 4Z" fill="#333"/><circle cx="6" cy="4" r="1.6" fill="#fff"/></symbol>
  <symbol id="lock" viewBox="0 0 8 10"><rect x="0" y="4" width="8" height="6" fill="#333"/><path d="M1.8 4 V2.6 A2.2 2.2 0 0 1 6.2 2.6 V4" stroke="#333" stroke-width="1.3" fill="none"/></symbol>
  <symbol id="folder" viewBox="0 0 14 11"><path d="M0.5 1 H5 L6.5 2.5 H13.5 V10.5 H0.5Z" fill="#ddd" stroke="#666"/></symbol>
</svg>

<ul class="layers">
  <li class="layer"><span class="vis"><svg width="11" height="8"><use href="#eye"/></svg></span><span class="thumb"></span>Light cookies</li>
  <li class="layer"><span class="vis"><svg width="11" height="8"><use href="#eye"/></svg></span><svg class="folder" width="14" height="11"><use href="#folder"/></svg>Text and Image with e...<svg class="lock" width="8" height="10"><use href="#lock"/></svg></li>
  <li class="layer is-editable"><span class="vis"><svg width="11" height="8"><use href="#eye"/></svg></span><span class="thumb photo"></span>ATHLETE IMAGE HERE</li>
  <li class="layer is-editable"><span class="vis"><svg width="11" height="8"><use href="#eye"/></svg></span><span class="thumb"></span>ADD TEXT HERE</li>
  <li class="layer is-editable"><span class="vis"><svg width="11" height="8"><use href="#eye"/></svg></span><span class="glyph-t">T</span>ATHLETE NAME</li>
  <li class="layer is-editable"><span class="vis"><svg width="11" height="8"><use href="#eye"/></svg></span><span class="thumb swatch"></span>QUILL COLORS</li>
  <li class="layer"><span class="vis"><svg width="11" height="8"><use href="#eye"/></svg></span><svg class="folder" width="14" height="11"><use href="#folder"/></svg>Quills<svg class="lock" width="8" height="10"><use href="#lock"/></svg></li>
  <li class="layer"><span class="vis"><svg width="11" height="8"><use href="#eye"/></svg></span><svg class="folder" width="14" height="11"><use href="#folder"/></svg>Background<svg class="lock" width="8" height="10"><use href="#lock"/></svg></li>
  <li class="layer"><span class="vis"><svg width="11" height="8"><use href="#eye"/></svg></span><span class="thumb white"></span><span class="italic">Background</span><svg class="lock" width="8" height="10"><use href="#lock"/></svg></li>
</ul>

</body>
</html>
```